Harbor of Mercy - Team of Rabbis and Doctors Helping Families Dealing with Illness

The Harbor of Mercy is an organization that accompanies families dealing with severe illnesses of a family member. A team of rabbis and doctors provide support and real-time responses to these families.
The site theme is medicine and law, but the target market is religious Jewish families in crisis. Thus, the site design needs to combine:
- professional, conservative, serious
- spiritual
- warm hug

Target Market(s)

religious families suffering a health crisis

Industry/Entity Type

Non-profit organization

Number of Pages Required

1 page

Font styles to use
Sans Serif

Requirements
Must have
• Final design in PSD format. List of fonts used, colors used and link/button colors used in the design.

```html
<!DOCTYPE html>
<html lang="en">
<head>
<meta charset="utf-8">
<title>Harbor of Mercy</title>
<link href="https://fonts.googleapis.com/css2?family=Inter:wght@300;400;600;700;800&family=Poppins:wght@300;400;500;600&display=swap" rel="stylesheet">
<style>
:root{
  --teal:#17b6ae;
  --teal-dark:#0f9a93;
  --teal-soft:#8fd8d3;
  --ink:#222a30;
  --text:#4a4f55;
  --muted:#7d848a;
  --dark:#1f2326;
  --darker:#16191b;
  --gold:#f5b21b;
  --white:#ffffff;
}
*{box-sizing:border-box;margin:0;padding:0}
html,body{width:1200px;height:4870px;overflow:hidden}
body{position:relative;background:var(--white);font-family:"Poppins",sans-serif;color:var(--text)}
.abs{position:absolute}
h1,h2,h3{font-family:"Inter",sans-serif}
.btn{position:absolute;display:flex;align-items:center;justify-content:center;background:var(--teal);color:var(--white);font-family:"Inter",sans-serif;font-weight:700;font-size:13px;text-transform:uppercase}
.eyebrow{position:absolute;font-family:"Inter",sans-serif;font-weight:600;font-size:17px;letter-spacing:4px;color:var(--teal)}
.photo{position:absolute}
.pulse-band{position:absolute;left:0;width:1200px;height:36px;background:linear-gradient(180deg,rgba(23,182,174,0) 0%,rgba(23,182,174,.35) 50%,rgba(23,182,174,0) 100%)}

/* top bar */
.topbar{position:absolute;left:0;top:0;width:1200px;height:42px;background:var(--teal);color:var(--white);font-family:"Inter",sans-serif;font-size:13px;font-weight:600;letter-spacing:1px}
.topbar .phone{position:absolute;left:193px;top:13px;letter-spacing:.5px}
.topbar .links{position:absolute;left:397px;top:13px}
.topbar .links span{margin:0 8px;opacity:.8}
.topbar .ask{position:absolute;left:805px;top:7px;width:153px;height:29px;border:1.5px solid var(--white);display:flex;align-items:center;justify-content:center;font-size:12px}
.topbar .donate{position:absolute;left:975px;top:7px;width:138px;height:29px;background:var(--dark);display:flex;align-items:center;justify-content:center;font-size:12px}

/* nav */
.nav{position:absolute;left:0;top:42px;width:1200px;height:108px}
.nav ul{position:absolute;left:130px;top:50px;display:flex;gap:30px;list-style:none;font-size:14px;color:var(--ink);font-weight:500}
.nav .active{border-bottom:2px solid var(--ink);padding-bottom:4px}
.brand{position:absolute;font-family:"Inter",sans-serif;font-weight:800;color:var(--teal);white-space:nowrap}

/* hero */
.hero{position:absolute;left:0;top:150px;width:1200px;height:505px;background:linear-gradient(100deg,#8fd6cc 0%,#c8e6d8 35%,#e9d6c4 60%,#d9cbbb 100%)}
.hero-title{position:absolute;left:92px;top:108px;color:var(--white);line-height:1}
.hero-title .l1{display:block;font-family:"Inter",sans-serif;font-weight:300;font-size:38px;margin-left:98px}
.hero-title .l2{display:block;font-family:"Inter",sans-serif;font-weight:800;font-size:52px;margin-top:10px}
.hero-title .l3{display:block;font-family:"Inter",sans-serif;font-weight:800;font-size:100px;margin-top:6px}

/* about */
.about-photo{left:85px;top:847px;width:527px;height:358px;border-radius:20px;background:linear-gradient(120deg,#f2f4f6,#d8dde2)}
.play{position:absolute;left:573px;top:985px;width:84px;height:84px;border-radius:50%;background:var(--teal);box-shadow:0 0 0 10px rgba(245,178,27,.15)}
.about-text{position:absolute;right:85px;top:840px;width:440px;text-align:right}
.about-text .title{font-family:"Inter",sans-serif;font-weight:800;font-size:46px;color:var(--teal);margin-top:14px}
.about-text .sub{font-size:17px;color:var(--ink);margin-top:6px}
.about-text p{font-size:13.5px;line-height:26px;margin-top:20px}

/* moral issues */
.moral{position:absolute;left:0;top:1333px;width:1200px;height:507px;background:linear-gradient(90deg,#18b7ae,#1ec3ba)}
.moral h2{position:absolute;left:222px;top:62px;font-size:44px;font-weight:800;color:var(--white)}
.issue{position:absolute;top:137px;width:245px;text-align:right;color:var(--white)}
.issue .pic{height:175px;border:3px solid var(--white);box-shadow:4px 4px 0 var(--teal-dark)}
.issue h3{font-size:14px;font-weight:700;margin-top:20px}
.issue p{font-size:13px;line-height:26px;margin-top:6px;opacity:.9}
.issue .link{display:inline-block;font-family:"Inter",sans-serif;font-size:12px;font-weight:700;text-decoration:underline;margin-top:12px}

/* services */
.service{position:absolute;top:1960px;width:237px;text-align:right}
.service .pic{height:180px;box-shadow:4px 4px 0 var(--teal-dark)}
.service h3{font-size:16px;font-weight:600;color:var(--teal);margin-top:28px}
.service p{font-size:13.5px;line-height:26px;color:var(--text);margin-top:4px}
.service .btn{position:relative;margin:22px 0 0 auto;width:145px;height:42px}

/* testimonials */
.testi{position:absolute;left:0;top:2415px;width:1200px;height:638px;background:var(--teal);color:var(--white);text-align:center}
.testi .eyebrow{left:0;width:1200px;top:66px;color:var(--white)}
.testi h2{position:absolute;left:0;width:1200px;top:98px;font-size:42px;font-weight:800}
.avatar{position:absolute;left:527px;top:170px;width:146px;height:140px;border:2px solid var(--white);border-radius:14px;padding:8px}
.avatar div{width:100%;height:100%;border-radius:8px;background:linear-gradient(#5b6a7a,#2f3c4a)}
.testi .name{position:absolute;left:0;width:1200px;top:335px;font-family:"Inter",sans-serif;font-weight:700;font-size:17px;letter-spacing:1px}
.testi .role{position:absolute;left:0;width:1200px;top:365px;font-size:13px;font-style:italic;opacity:.9}
.testi .quote{position:absolute;left:260px;width:680px;top:385px;font-size:20px;line-height:36px;font-weight:300}
.thumbs{position:absolute;left:333px;top:527px;display:flex;gap:21px}
.thumbs div{width:72px;height:72px;border:2px solid var(--white);border-radius:8px;padding:4px}
.thumbs div span{display:block;width:100%;height:100%;border-radius:5px;background:linear-gradient(#a8b4be,#56606b)}

/* news */
.news-card{position:absolute;top:3268px;width:322px;height:437px;background:var(--white);box-shadow:0 6px 22px rgba(0,0,0,.10);text-align:center}
.news-card .pic{height:225px}
.news-card h3{font-size:17px;font-weight:700;color:var(--teal);line-height:25px;margin:15px 20px 0}
.news-card p{font-size:13.5px;line-height:23px;margin:15px 25px 0}
.news-card .btn{left:149px;top:380px;width:145px;height:45px}
.outline-btn{position:absolute;left:85px;top:3190px;width:147px;height:49px;border:2px solid var(--teal);color:var(--teal);font-family:"Inter",sans-serif;font-size:13px;font-weight:700;display:flex;align-items:center;justify-content:center}
.section-title{position:absolute;right:85px;font-size:44px;font-weight:800;color:var(--teal)}

/* form */
.field{position:absolute;left:280px;width:640px;height:45px;border:1.5px solid #b8bec4;display:flex;align-items:center;padding-left:16px;font-size:14px;color:#8d949a;gap:10px}
.field.area{height:115px;align-items:flex-start;padding-top:12px}

/* footer */
.footer{position:absolute;left:0;top:4460px;width:1200px;height:410px;background:var(--dark);color:#c8ccd0}
.footer h4{font-family:"Inter",sans-serif;font-size:14px;font-weight:700;letter-spacing:2.5px;color:var(--white);position:absolute;text-align:center}
.footer .small{position:absolute;font-size:13px;color:#a7adb2}
.footer .divider{position:absolute;top:95px;width:2px;height:185px;background:#3d4347}
.footer .divider::before{content:"";position:absolute;left:-1px;top:20px;width:4px;height:28px;background:var(--gold)}
.bottombar{position:absolute;left:0;top:350px;width:1200px;height:60px;background:var(--darker);font-size:13px;color:#8f969b}
</style>
</head>
<body>

<!-- Top bar -->
<div class="topbar">
  <svg class="abs" style="left:84px;top:14px" width="16" height="16" viewBox="0 0 16 16"><circle cx="6.5" cy="6.5" r="5" fill="none" stroke="#fff" stroke-width="2"/><path d="M10 10l4.5 4.5" stroke="#fff" stroke-width="2"/></svg>
  <svg class="abs" style="left:122px;top:14px" width="16" height="16" viewBox="0 0 16 16"><rect x="1" y="1" width="14" height="14" rx="3" fill="none" stroke="#fff" stroke-width="1.6"/></svg>
  <svg class="abs" style="left:160px;top:9px" width="20" height="24" viewBox="0 0 20 24"><rect width="20" height="24" rx="3" fill="#0f9a93"/><path d="M6 6c0 7 3 11 8 12l1.5-2.5-3-2-1.5 1.5c-1.5-1-2.5-2.5-3-4.5L9.5 9 8 6z" fill="#fff"/></svg>
  <span class="phone">070-5550123</span>
  <div class="links">24/7 HOTLINE<span>|</span>DEDICATION 2<span>|</span>DEDICATION 1</div>
  <div class="ask">ASK THE RABBI</div>
  <div class="donate">DONATE NOW</div>
</div>

<!-- Navigation -->
<div class="nav">
  <svg class="abs" style="left:87px;top:52px" width="20" height="20" viewBox="0 0 20 20"><rect width="9" height="9" fill="#17b6ae"/><rect x="11" width="9" height="9" fill="#17b6ae"/><rect y="11" width="9" height="9" fill="#17b6ae"/><rect x="11" y="11" width="9" height="9" fill="#17b6ae"/></svg>
  <ul>
    <li>Contact</li><li>Courses and traing</li><li>The&nbsp; world of knowledge</li><li>Question and Answers</li><li>About</li><li class="active">Home</li>
  </ul>
  <div class="brand" style="right:85px;top:45px;font-size:22px">Harbor of Mercy</div>
</div>

<!-- Hero -->
<section class="hero" role="img" aria-label="Photo of a caring hand resting gently on an elderly patient's hand">
  <h1 class="hero-title"><span class="l1">Should Morphine</span><span class="l2">be given to the</span><span class="l3">Patient?</span></h1>
  <div class="abs" role="img" aria-label="Decorative row of books" style="left:948px;top:400px;width:242px;height:95px;background:linear-gradient(90deg,#13a59d,#17b6ae);opacity:.85"></div>
</section>
<div class="pulse-band" style="top:640px" role="img" aria-label="Decorative heartbeat line"></div>

<!-- About -->
<div class="photo about-photo" role="img" aria-label="Photo of a stethoscope on a white surface"></div>
<div class="play"><svg width="84" height="84" viewBox="0 0 84 84"><circle cx="42" cy="42" r="18" fill="none" stroke="#f5b21b" stroke-width="2"/><path d="M37 33l13 9-13 9z" fill="none" stroke="#f5b21b" stroke-width="2"/></svg></div>
<div class="about-text">
  <div style="font-family:Inter,sans-serif;font-weight:600;font-size:17px;letter-spacing:4px;color:var(--teal)">ABOUT</div>
  <div class="title">Harbor of Mercy</div>
  <div class="sub">Law and ethics in complex medical conditions</div>
  <p>The Harbor of Mercy' is a project that offers solutions' to families who need to decide on complex and urgent halachic questions regarding a family member who is in danger of life or in complex medical conditions. Among other things, the project operates an open telephone</p>
</div>
<div class="btn" style="left:955px;top:1135px;width:160px;height:45px">READ MORE</div>

<!-- More Moral Issues -->
<section class="moral">
  <h2>More Moral Issues</h2>
  <div class="issue" style="left:85px">
    <div class="pic" role="img" aria-label="Photo of laboratory equipment" style="background:linear-gradient(#e6ebee,#9aa6ad)"></div>
    <h3>The vision of the harbor of mercy</h3>
    <p>Our vision is related to these three partners:&nbsp; the family</p>
    <span class="link">DONATE NOW</span>
  </div>
  <div class="issue" style="left:355px">
    <div class="pic" role="img" aria-label="Photo of a hand touching a digital healthcare icon" style="background:linear-gradient(#7fb8c9,#3d6a7c)"></div>
    <h3>The vision of the harbor of mercy</h3>
    <p>Our vision is related to these three partners:&nbsp; the family</p>
    <span class="link">DONATE NOW</span>
  </div>
  <div class="abs" role="img" aria-label="Faint decorative books" style="left:0;top:415px;width:190px;height:92px;background:rgba(255,255,255,.12)"></div>
  <div class="photo" role="img" aria-label="Portrait photo of the rabbi with signature" style="left:650px;top:67px;width:485px;height:440px;background:linear-gradient(#2c3b44,#17242b)"></div>
</section>

<!-- Services -->
<div class="service" style="left:85px"><div class="pic" role="img" aria-label="Photo of a course group" style="background:linear-gradient(#d6dade,#8a8f93)"></div><h3>Courses</h3><p>Nunc pharetra elit nec est dictum suscipit. Vestibulum non</p><div class="btn">READ MORE</div></div>
<div class="service" style="left:350px"><div class="pic" role="img" aria-label="Photo of a conference meeting" style="background:linear-gradient(#c7b49c,#7c6a56)"></div><h3>Conferences</h3><p>Nunc pharetra elit nec est dictum suscipit. Vestibulum non</p><div class="btn">READ MORE</div></div>
<div class="service" style="left:615px"><div class="pic" role="img" aria-label="Photo of a lecture hall" style="background:linear-gradient(#e1e4e6,#8f969c)"></div><h3>Lectures</h3><p>Nunc pharetra elit nec est dictum suscipit. Vestibulum non</p><div class="btn">READ MORE</div></div>
<div class="service" style="left:880px"><div class="pic" role="img" aria-label="Photo of a hotline operator with headset" style="background:linear-gradient(#f0f1f2,#b7bcc0)"></div><h3>Hotline 24/7</h3><p>Nunc pharetra elit nec est dictum suscipit. Vestibulum non</p><div class="btn">READ MORE</div></div>

<!-- Testimonials -->
<svg class="abs" style="left:210px;top:3050px" width="200" height="85" viewBox="0 0 200 85"><path d="M0 0H200L0 85z" fill="#17b6ae"/></svg>
<section class="testi">
  <div class="eyebrow">TESTIMONIALS</div>
  <h2>What Our Client Says</h2>
  <svg class="abs" style="left:353px;top:215px" width="60" height="52" viewBox="0 0 60 52"><path d="M0 26C0 10 8 2 22 0v10c-7 2-10 6-10 12h10v30H0zM34 26C34 10 42 2 56 0v10c-7 2-10 6-10 12h10v30H34z" fill="#fff"/></svg>
  <svg class="abs" style="left:787px;top:215px" width="60" height="52" viewBox="0 0 60 52"><path d="M60 26C60 42 52 50 38 52V42c7-2 10-6 10-12H38V0h22zM26 26C26 42 18 50 4 52V42c7-2 10-6 10-12H4V0h22z" fill="#fff"/></svg>
  <div class="avatar"><div role="img" aria-label="Client portrait"></div></div>
  <svg class="abs" style="left:112px;top:290px" width="34" height="60" viewBox="0 0 34 60"><path d="M30 2L4 30l26 28" fill="none" stroke="#8fd8d3" stroke-width="2.5"/></svg>
  <svg class="abs" style="left:1054px;top:290px" width="34" height="60" viewBox="0 0 34 60"><path d="M4 2l26 28L4 58" fill="none" stroke="#8fd8d3" stroke-width="2.5"/></svg>
  <div class="name">DANIEL REED</div>
  <div class="role">Simply Dummy</div>
  <div class="quote">Quis ipsum suspendisse ultrices gravida. Risus commodo viverra maecenas accumsan lacus vel facilisis. Aliquam congue in felis id egestas. Pellentesque habitant morbi tristique senectus.</div>
  <svg class="abs" style="left:535px;top:497px" width="130" height="20" viewBox="0 0 130 20">
    <g fill="#f5b21b">
      <path id="star" d="M10 0l3 6.5 7 .8-5.2 4.8 1.4 7L10 15.6 3.8 19.1l1.4-7L0 7.3l7-.8z"/>
      <use href="#star" x="27"/><use href="#star" x="54"/><use href="#star" x="81"/><use href="#star" x="108"/>
    </g>
  </svg>
  <div class="thumbs">
    <div><span role="img" aria-label="Client portrait"></span></div>
    <div><span role="img" aria-label="Client portrait"></span></div>
    <div><span role="img" aria-label="Client portrait"></span></div>
    <div><span role="img" aria-label="Client portrait"></span></div>
    <div><span role="img" aria-label="Client portrait"></span></div>
    <div><span role="img" aria-label="Client portrait"></span></div>
  </div>
</section>

<!-- News -->
<div class="eyebrow" style="right:85px;top:3160px">NEWS</div>
<h2 class="section-title" style="top:3188px">Latest news and articles</h2>
<div class="outline-btn">VIEW ALL NEWS</div>
<article class="news-card" style="left:85px"><div class="pic" role="img" aria-label="Photo of a gavel and scales of justice" style="background:linear-gradient(#4a4d50,#1f2123)"></div><h3>Aenean blandit lobortis finibus aliquam nislerat malesuada</h3><p>Aenean pretium molestie nisl, et rices urna ultrsit amet. Integer at tellus vel</p><div class="btn">READ MORE</div></article>
<article class="news-card" style="left:438px"><div class="pic" role="img" aria-label="Photo of a vaccine syringe" style="background:linear-gradient(#d6e6f2,#7fa4c2)"></div><h3>Aenean blandit lobortis finibus aliquam nislerat malesuada</h3><p>Aenean pretium molestie nisl, et rices urna ultrsit amet. Integer at tellus vel</p><div class="btn">READ MORE</div></article>
<article class="news-card" style="left:790px"><div class="pic" role="img" aria-label="Photo of a family outdoors" style="background:linear-gradient(#a6ad9a,#4f5546)"></div><h3>Aenean blandit lobortis finibus aliquam nislerat malesuada</h3><p>Aenean pretium molestie nisl, et rices urna ultrsit amet. Integer at tellus vel</p><div class="btn">READ MORE</div></article>

<!-- Contact form -->
<div class="eyebrow" style="right:85px;top:3810px">CONTACT FORM</div>
<h2 class="section-title" style="top:3838px">Ask the Rabbi</h2>
<div class="field" style="top:3935px"><svg width="14" height="14" viewBox="0 0 14 14"><circle cx="7" cy="4" r="3" fill="#a3aab0"/><path d="M1 14c0-4 3-6 6-6s6 2 6 6z" fill="#a3aab0"/></svg>Name:</div>
<div class="field" style="top:3997px"><svg width="14" height="12" viewBox="0 0 14 12"><rect x=".5" y=".5" width="13" height="11" fill="none" stroke="#a3aab0"/><path d="M.5 .5l6.5 6 6.5-6" fill="none" stroke="#a3aab0"/></svg>Email:</div>
<div class="field" style="top:4058px"><svg width="14" height="14" viewBox="0 0 14 14"><path d="M2 1c0 7 4 11 11 12l1-3-3-2-2 2C7 9 5 7 4 5l2-2-2-3z" fill="none" stroke="#a3aab0"/></svg>Phone:</div>
<div class="field area" style="top:4120px"><svg width="14" height="14" viewBox="0 0 14 14"><path d="M1 1h12v9H5l-3 3v-3H1z" fill="none" stroke="#a3aab0"/></svg>Comments:</div>
<div class="btn" style="left:280px;top:4250px;width:147px;height:45px">SUBMIT NOW</div>

<!-- Footer -->
<div class="abs" role="img" aria-label="Decorative row of books" style="left:965px;top:4340px;width:230px;height:95px;background:linear-gradient(90deg,#2a3034,#1f2326)"></div>
<div class="pulse-band" style="top:4415px" role="img" aria-label="Decorative heartbeat line"></div>
<footer class="footer">
  <h4 style="left:85px;width:330px;top:118px">SUBSCRIBE NEWSLETTER</h4>
  <div class="small" style="left:85px;width:330px;top:143px;text-align:center">Subscribe our newsletter for update</div>
  <div class="abs" style="left:85px;top:165px;width:330px;height:43px;background:#fff;display:flex;align-items:center;justify-content:flex-end;padding-right:12px;gap:10px;font-size:13px;color:#a3aab0">Enter email address <svg width="14" height="12" viewBox="0 0 14 12"><rect x=".5" y=".5" width="13" height="11" fill="none" stroke="#a3aab0"/><path d="M.5 .5l6.5 6 6.5-6" fill="none" stroke="#a3aab0"/></svg></div>
  <div class="btn" style="left:270px;top:225px;width:145px;height:43px">SUBSCRIBE</div>
  <div class="divider" style="left:487px"></div>
  <h4 style="left:560px;width:280px;top:118px">CONTACT US</h4>
  <div class="small" style="left:510px;width:220px;top:155px;text-align:right;line-height:24px">Institute address: Cedar Lane 12, Riverton</div>
  <svg class="abs" style="left:748px;top:160px" width="12" height="15" viewBox="0 0 12 15"><path d="M6 14s5-5 5-8.5A5 5 0 001 5.5C1 9 6 14 6 14z" fill="none" stroke="#f5b21b" stroke-width="1.5"/><circle cx="6" cy="5.5" r="1.8" fill="#f5b21b"/></svg>
  <div class="small" style="left:510px;width:220px;top:215px;text-align:right">info@harborofmercy.org</div>
  <svg class="abs" style="left:746px;top:218px" width="15" height="12" viewBox="0 0 15 12"><rect x=".75" y=".75" width="13.5" height="10.5" fill="none" stroke="#f5b21b" stroke-width="1.5"/><path d="M.75 .75l6.75 6 6.75-6" fill="none" stroke="#f5b21b" stroke-width="1.5"/></svg>
  <div class="small" style="left:510px;width:220px;top:255px;text-align:right">70-5550-123</div>
  <svg class="abs" style="left:746px;top:257px" width="14" height="14" viewBox="0 0 14 14"><path d="M2 1c0 7 4 11 11 12l1-3-3-2-2 2C7 9 5 7 4 5l2-2-2-3z" fill="#f5b21b"/></svg>
  <div class="divider" style="left:828px"></div>
  <div class="brand" style="left:890px;top:140px;font-size:26px">Harbor of Mercy</div>
  <div class="bottombar">
    <div class="abs" style="left:85px;top:21px">© 2023 <span style="color:var(--gold)">Harbor of Mercy</span> . All right reserved</div>
    <div class="abs" style="right:85px;top:21px">December 13, 2023. Layout_4</div>
  </div>
</footer>

</body>
</html>
```